Website for Plumbing Company, Sir FlowBoiler

I need a 7-page fully HTML-coded website for my plumbing company, Sir FlowBoiler. We specialize in installation, repair, and replacement of both gas and electric water heaters. Although we offer both tankless (on-demand) water heaters and standard (with tank) water heaters, most of our business is related to standard (with tank) water heaters in the USA market.

These are the pages I need:
1. Home page with sections such as About Us, Our Services, Why Choose Us, Testimonials, Location Map (Palm Beach County Florida), Quote Request Form, Join Our Newsletter, Mission Statement, etc.

2. Gas Water Heaters

3. Electric Water Heaters

4. Tankless Water Heaters

5. About Us

6. Contact Us

7. Privacy Policy, Terms & Conditions

Be sure to mention the following points:
1. Same-Day Service
2. Best Price Guarantee
3. 100% Satisfaction Rating
4. 15-Year Warranty on Water Heater & Parts
5. Lifetime Warranty on Workmanship
*All Warranties are Transferrable Upon Home Sale

Once design is selected and finalized, I need the website coded in a standard HTML/CSS and temporarily hosted on your development server so I can see the website functionality that is not observable from screenshots, such as section animations, etc. Once those details are finalized, I will move the source code to my server and complete the project.

Target Market(s)

Residential Home Owners and Business Owners

Industry/Entity Type

Plumbing, Home Services, Remodeling, Construction

Coding

Coded - Design and coding required

Number of Pages Required

5+ page

Colors
0054AA
0677BA
7BADD7
CADEEF
E8F1F8
FFC000
F8CF3A
FAE287
FDF2CF
FEFAEE
EE7325
F08F49
F5BC92
FAE3D3
FDF4ED

Requirements
Must have
• Clean, colorful, and professional

```html
<!DOCTYPE html>
<html lang="en">
<head>
<meta charset="utf-8">
<title>Sir FlowBoiler – Water Heater Experts</title>
<link href="https://fonts.googleapis.com/css2?family=Inter:wght@400;500;600;700;800&display=swap" rel="stylesheet">
<style>
:root{
  --navy:#1d2340;
  --blue:#0054aa;
  --royal:#243c8f;
  --slate:#3e4a78;
  --orange:#ee7325;
  --orange-soft:#f08f49;
  --sky:#7badd7;
  --ice:#e8f1f8;
  --gray-bg:#f3f3f4;
  --text:#222;
  --muted:#555;
  --white:#fff;
}
*{box-sizing:border-box;margin:0;padding:0}
html,body{width:1200px;height:4834px;overflow:hidden}
body{font-family:'Inter',sans-serif;color:var(--text);background:var(--white);position:relative}
section,header,footer,.topbar{position:relative;width:1200px}
.abs{position:absolute}
a{color:inherit;text-decoration:none}
.btn{display:inline-flex;align-items:center;justify-content:center;gap:8px;border-radius:30px;font-weight:600;font-size:15px;height:36px;padding:0 26px}
.btn-solid{background:var(--orange);color:#fff}
.btn-line{border:2px solid var(--orange);color:var(--orange);background:#fff}
.brand{font-weight:800;font-size:24px;color:var(--blue);display:flex;align-items:center;gap:10px}
.brand .dot{width:34px;height:34px;border-radius:50%;background:var(--orange)}

/* top bar */
.topbar{height:30px;background:var(--navy);color:#fff;font-size:12px}
.topbar .left{left:68px;top:8px;display:flex;align-items:center;gap:6px}
.topbar .left i{width:7px;height:7px;border-radius:50%;background:var(--orange);display:block}
.topbar .right{right:68px;top:7px;display:flex;gap:28px;align-items:center}
.topbar .right span{display:flex;gap:8px;align-items:center}

/* nav */
.site-nav{height:60px;background:#fff}
.site-nav .brand{left:68px;top:12px}
.site-nav ul{list-style:none;left:405px;top:21px;display:flex;gap:32px;font-size:13px;font-weight:500}
.site-nav ul li.active{color:#1f6fe0}
.site-nav .actions{right:50px;top:12px;display:flex;gap:12px}
.site-nav .actions .btn{height:30px;font-size:13px;padding:0 20px;font-weight:500}

/* hero */
.hero{height:586px;background:linear-gradient(100deg,#27291f 0%,#45493c 35%,#8b94a0 60%,#c7cdd3 100%);color:#fff;overflow:hidden}
.hero .photo{inset:0}
.hero .shade{inset:0;background:linear-gradient(90deg,rgba(0,0,0,.55) 0%,rgba(0,0,0,.25) 45%,rgba(0,0,0,0) 70%)}
.hero .tag{left:68px;top:126px;font-size:14px;font-weight:700;display:flex;gap:6px;align-items:center}
.hero h1{left:68px;top:176px;font-size:52px;line-height:66px;font-weight:800;letter-spacing:-.5px}
.hero h1 em{font-style:normal;color:#ffa60f}
.hero .ctas{left:68px;top:352px;display:flex;gap:22px}
.hero .ctas .btn-ghost{border:2px solid #fff;color:#fff}
.hero .services{left:68px;top:434px;display:flex;gap:14px;align-items:center;font-size:14px;font-weight:500}
.hero .services i{width:6px;height:6px;border-radius:50%;background:#fff;display:block}

/* about */
.about{height:526px;background:var(--gray-bg)}
.about .house{left:68px;top:28px}
.about .img-team{left:95px;top:96px;width:296px;height:280px;background:linear-gradient(160deg,#c8d2dc,#3d5d9a 60%,#b44b35);border-radius:3px}
.about .img-tech{left:404px;top:177px;width:210px;height:220px;background:linear-gradient(160deg,#d8d4cc,#9aa0a8 50%,#c5452f);border-radius:3px}
.about h2{left:646px;top:114px;font-size:38px;font-weight:700;color:var(--royal)}
.about h2 em{font-style:normal;color:var(--orange)}
.about p{left:646px;width:480px;font-size:16px;line-height:21px;color:#333}
.about .p1{top:192px}
.about .p2{top:318px}
.about .ctas{left:646px;top:426px;display:flex;gap:18px}
.features{left:98px;top:1180px;width:995px;height:84px;background:var(--royal);border-radius:4px;display:flex;justify-content:center;align-items:center;gap:44px;color:#fff;font-size:17px;font-weight:500;z-index:2}
.features span{display:flex;gap:10px;align-items:center}

/* services */
.services-sec{height:708px;background:#fff}
.services-sec h2{width:100%;text-align:center;top:132px;font-size:29px;font-weight:700;color:var(--royal)}
.card{top:179px;width:310px}
.card .pic{width:310px;height:310px;background:var(--gray-bg);border-radius:2px}
.card h3{margin-top:22px;font-size:22px;font-weight:700}
.card p{margin-top:18px;font-size:14px;line-height:18px;color:#333;width:270px;height:36px}
.card .btn{margin-top:30px;height:36px;font-size:14px}

/* why */
.why{height:676px;background:var(--slate);color:#fff}
.why h2{width:100%;text-align:center;top:76px;font-size:38px;font-weight:700}
.why .rule{left:200px;width:800px;height:1px;background:rgba(255,255,255,.18)}
.why h3{width:100%;text-align:center;top:171px;font-size:30px;font-weight:600}
.why .lead{left:215px;width:770px;top:227px;text-align:center;font-size:14px;line-height:18px;color:#d5d9e6}
.why .item{display:flex;gap:26px;align-items:flex-start}
.why .item h4{font-size:22px;font-weight:500}
.why .item p{font-size:14px;color:#c9cde0;margin-top:14px}

/* testimonials */
.reviews{height:509px;background:#fff}
.reviews h2{width:100%;text-align:center;top:44px;font-size:30px;font-weight:700;line-height:40px}
.reviews .platform{width:100%;top:188px;display:flex;justify-content:center;align-items:center;gap:8px;font-size:22px;font-weight:500}
.reviews .platform i{display:block;width:18px;height:18px;border-radius:50%;background:var(--royal)}
.reviews .rule{left:375px;width:450px;top:229px;height:1px;background:#e3e3e3}
.reviews blockquote{left:380px;width:440px;top:245px;text-align:center;font-size:14px;font-weight:600;color:#445;line-height:20px}
.reviews .arrow{width:28px;height:28px;border-radius:50%;top:276px}
.reviews .name{width:100%;text-align:center;top:340px;font-size:20px;font-weight:600}
.reviews .place{width:100%;text-align:center;top:376px;font-size:14px;font-weight:600}
.reviews .stars{width:100%;top:396px;display:flex;justify-content:center;gap:4px}
.reviews .dots{width:100%;top:452px;display:flex;justify-content:center;gap:6px;align-items:center}
.reviews .dots i{display:block;width:6px;height:6px;border-radius:50%;background:#ccd}
.reviews .dots i.on{width:24px;border-radius:4px;background:var(--royal)}

/* contact */
.contact{height:890px;background:var(--royal);color:#fff}
.contact h2{width:100%;text-align:center;top:48px;font-size:30px;font-weight:700}
.contact .sub{width:100%;text-align:center;top:110px;font-size:22px;font-weight:500}
.contact .map{left:60px;top:196px;width:428px;height:616px;border-radius:14px;background:linear-gradient(150deg,#4e5d45,#2f3b33 40%,#5b6a56 70%,#3a4537);overflow:hidden}
.contact .map .label{left:14px;top:20px;font-size:15px;display:flex;align-items:center;gap:6px}
.contact .map .note{left:70px;bottom:20px;width:340px;height:70px;background:var(--royal);border-radius:12px;font-size:13px;line-height:22px;padding:12px 26px}
.contact .map .note u{font-weight:600;font-size:14px}
.contact .map .pin{left:22px;bottom:40px;width:30px;height:30px;border-radius:50%;background:var(--royal);display:flex;align-items:center;justify-content:center}
.quote{left:514px;top:196px;width:618px;height:616px;background:#fff;border-radius:14px;color:var(--text)}
.quote h3{width:100%;text-align:center;top:46px;font-size:23px;font-weight:600;color:var(--royal)}
.quote label{font-size:12px;font-weight:500}
.quote .field{height:38px;border:1px solid #b9bcc6;border-radius:2px;font-size:10px;color:#888;padding:0 10px;display:flex;align-items:center;margin-top:6px}
.quote .field.area{height:130px;align-items:flex-start;padding-top:10px}
.quote .field.select{color:#222;font-size:12px;justify-content:space-between}
.quote .submit{left:199px;top:537px;width:220px;height:38px;font-size:14px}

/* cta */
.cta{height:432px;background:#fff;overflow:hidden}
.cta h2{left:62px;top:70px;font-size:42px;line-height:48px;font-weight:700;color:#333;width:600px}
.cta .links{left:62px;top:233px;display:flex;gap:14px;align-items:center;font-size:15px;color:var(--blue);font-weight:500}
.cta .links i{display:block;width:5px;height:5px;border-radius:50%;background:var(--blue)}
.cta .btn{left:62px;top:290px;height:38px;padding:0 6px 0 24px;font-size:15px}
.cta .btn .ring{width:30px;height:30px;border-radius:50%;background:#fff;display:flex;align-items:center;justify-content:center}
.cta .photo{left:714px;top:0;width:486px;height:432px;background:linear-gradient(90deg,#f3f3f3 0%,#b9bec5 25%,#2c4f92 50%,#d8473a 62%,#8a9098 80%,#f3f3f3 100%)}

/* footer */
.site-footer{height:417px;background:var(--navy);color:#fff}
.site-footer .contact-row .c{display:flex;gap:18px;align-items:center;top:47px}
.site-footer .ico{width:46px;height:46px;border-radius:50%;background:rgba(255,255,255,.08);display:flex;align-items:center;justify-content:center}
.site-footer .c small{display:block;font-size:10px;margin-bottom:8px}
.site-footer .c span{font-size:13px}
.site-footer .brand{left:42px;top:216px;color:#fff;font-size:22px}
.site-footer .col{top:176px}
.site-footer .col h4{font-size:19px;font-weight:500;margin-bottom:22px}
.site-footer .col li{list-style:none;font-size:12px;color:#c7cad6;margin-bottom:14px}
.site-footer .social{display:flex;gap:10px}
.site-footer .social i{display:block;width:26px;height:26px;border-radius:50%;border:1.5px solid var(--orange)}
.site-footer .copy{width:100%;text-align:center;top:377px;font-size:10px;color:#c7cad6}
</style>
</head>
<body>

<div class="topbar">
  <div class="abs left"><i></i>Same-Day Service</div>
  <div class="abs right">
    <span><svg width="12" height="12" viewBox="0 0 24 24" fill="#fff"><path d="M6.6 10.8a15 15 0 0 0 6.6 6.6l2.2-2.2c.3-.3.7-.4 1-.2 1.1.4 2.3.6 3.6.6.6 0 1 .4 1 1V20c0 .6-.4 1-1 1A17 17 0 0 1 3 4c0-.6.4-1 1-1h3.5c.6 0 1 .4 1 1 0 1.3.2 2.5.6 3.6.1.3 0 .7-.2 1z"/></svg>(555)-0142-7781</span>
    <span><svg width="13" height="10" viewBox="0 0 24 18" fill="#fff"><path d="M0 0h24v18H0z"/><path d="M0 0l12 9 12-9" stroke="#1d2340" stroke-width="2" fill="none"/></svg>info@sirflowboiler.com</span>
  </div>
</div>

<header class="site-nav">
  <div class="abs brand"><span class="dot"></span>Sir FlowBoiler</div>
  <ul class="abs">
    <li class="active">Home</li><li>Water Heaters</li><li>About Us</li><li>Contact Us</li><li>T&amp;C</li>
  </ul>
  <div class="abs actions">
    <a class="btn btn-solid">Request Quote Now</a>
    <a class="btn btn-line">Contact Now</a>
  </div>
</header>

<section class="hero">
  <div class="abs photo" role="img" aria-label="Smiling technician in cap and overalls standing with arms crossed before a branded service van"></div>
  <div class="abs shade"></div>
  <div class="abs tag"><svg width="10" height="13" viewBox="0 0 10 13"><path d="M5 0C6 3 9 5 9 8.5A4 4 0 0 1 1 8.5C1 6 3 5 3 3 4 4 5 5 5 0z" fill="#ffa60f"/></svg>SAME-DAY SERVICE AVAILABLE</div>
  <h1 class="abs">Palm Beach County's #1<br><em>Water Heater Experts</em></h1>
  <div class="abs ctas">
    <a class="btn btn-solid">Request Quote</a>
    <a class="btn btn-ghost" style="padding:0 6px 0 22px">Call Us Now <svg width="24" height="24" viewBox="0 0 24 24"><circle cx="12" cy="12" r="11" fill="none" stroke="#fff" stroke-width="1.5"/><path d="M9 7.5l1.6 2.6-1 1c.6 1.3 1.6 2.3 2.9 2.9l1-1 2.5 1.6-.8 1.5c-3.6-.3-6.5-3.2-6.8-6.8z" fill="#fff"/></svg></a>
  </div>
  <div class="abs services">Installation <i></i> Repair <i></i> Replacements</div>
</section>

<section class="about">
  <svg class="abs house" width="310" height="330" viewBox="0 0 310 330"><path d="M0 90 L178 0 L310 70 L310 330 L0 330z" fill="#dcdcde"/></svg>
  <div class="abs img-team" role="img" aria-label="Technician in blue shirt standing in a showroom of wall-mounted tankless water heaters"></div>
  <div class="abs img-tech" role="img" aria-label="Technician adjusting the controls of a gas tank water heater"></div>
  <h2 class="abs">About <em>Sir FlowBoiler</em></h2>
  <p class="abs p1">At Sir FlowBoiler, we specialize in fast, reliable installation, repair, and replacement of gas, electric, and tankless water heaters. With decades of experience and a 100% satisfaction rating, we've earned the trust of homeowners and businesses across Florida.</p>
  <p class="abs p2">'Our team of licensed professionals treats every home and business like our own. We believe in transparent pricing, quality workmanship, and customer satisfaction above all else.'</p>
  <div class="abs ctas">
    <a class="btn btn-solid">Contact Us</a>
    <a class="btn btn-line">Learn More About Us</a>
  </div>
</section>

<div class="abs features">
  <span><svg width="16" height="12" viewBox="0 0 16 12"><path d="M1 6l5 5L15 1" fill="none" stroke="#4fd07a" stroke-width="2"/></svg>Same Day Service</span>
  <span><svg width="16" height="12" viewBox="0 0 16 12"><path d="M1 6l5 5L15 1" fill="none" stroke="#4fd07a" stroke-width="2"/></svg>Best Price Guarantee</span>
  <span><svg width="16" height="12" viewBox="0 0 16 12"><path d="M1 6l5 5L15 1" fill="none" stroke="#4fd07a" stroke-width="2"/></svg>100% Satisfaction</span>
  <span><svg width="16" height="12" viewBox="0 0 16 12"><path d="M1 6l5 5L15 1" fill="none" stroke="#4fd07a" stroke-width="2"/></svg>15–Years Warranty</span>
</div>

<section class="services-sec">
  <h2 class="abs">Expert Water Heater Services</h2>
  <div class="abs card" style="left:115px">
    <div class="pic" role="img" aria-label="Gray gas tank water heater"></div>
    <h3>Gas Water Heaters</h3>
    <p>Professional installation and repair of gas-powered water heaters</p>
    <a class="btn btn-line">Learn More</a>
  </div>
  <div class="abs card" style="left:445px">
    <div class="pic" role="img" aria-label="White electric water heater unit with digital display"></div>
    <h3>Electric Water Heaters</h3>
    <p>Energy-efficient electric water heater solutions</p>
    <a class="btn btn-line">Learn More</a>
  </div>
  <div class="abs card" style="left:776px">
    <div class="pic" role="img" aria-label="White wall-mounted tankless water heater"></div>
    <h3>Tankless Water Heaters</h3>
    <p>On-demand hot water with space-saving tankless systems</p>
    <a class="btn btn-line">Learn More</a>
  </div>
</section>

<section class="why">
  <h2 class="abs">Why Choose Sir FlowBoiler</h2>
  <div class="abs rule" style="top:152px"></div>
  <h3 class="abs">Fast, Reliable, and Satisfaction Guaranteed</h3>
  <p class="abs lead">Whether it's a sudden leak or a planned upgrade, Sir FlowBoiler is your trusted partner for water heater services in Palm Beach County. We combine expert workmanship with unbeatable warranties and same-day service to keep your home running smoothly.</p>
  <div class="abs rule" style="top:329px"></div>

  <div class="abs item" style="left:145px;top:375px">
    <svg width="52" height="52" viewBox="0 0 52 52" fill="none" stroke="#b9bfd6" stroke-width="2.5"><circle cx="26" cy="26" r="22"/><circle cx="26" cy="26" r="14"/><path d="M26 18v8l6 4"/></svg>
    <div><h4>Same Day Services</h4><p>Quick, professional services same day !</p></div>
  </div>
  <div class="abs item" style="left:636px;top:375px">
    <svg width="52" height="52" viewBox="0 0 52 52" fill="none" stroke="#b9bfd6" stroke-width="2.5"><circle cx="26" cy="20" r="14"/><path d="M19 20l5 5 9-9M16 31l-6 14 7-2 4 6 5-12M36 31l6 14-7-2-4 6-5-12"/></svg>
    <div><h4>Lifetime Workmanship Warranty</h4><p>Transferable upon home sale.</p></div>
  </div>
  <div class="abs item" style="left:145px;top:527px">
    <svg width="52" height="52" viewBox="0 0 52 52" fill="none" stroke="#b9bfd6" stroke-width="2.5"><path d="M26 6a20 20 0 1 0 8 38"/><path d="M26 14v18l-7-7M26 32l7-7"/><circle cx="40" cy="40" r="9"/><path d="M43 36h-5a2 2 0 0 0 0 4h4a2 2 0 0 1 0 4h-5"/></svg>
    <div><h4>Best Price Guarantee</h4><p>We offer competitive pricing with no hidden fees.</p></div>
  </div>
  <div class="abs item" style="left:636px;top:527px">
    <svg width="52" height="52" viewBox="0 0 52 52" fill="none" stroke="#b9bfd6" stroke-width="2.5"><path d="M26 38s-12-11-12-20a12 12 0 0 1 24 0c0 9-12 20-12 20z"/><circle cx="26" cy="18" r="5"/><path d="M14 36l-8 10h40l-8-10"/></svg>
    <div><h4>Locally Owned &amp; Operated</h4><p>Serving Palm Beach County.</p></div>
  </div>
</section>

<section class="reviews">
  <h2 class="abs">What Our Customers Say<br>About Us</h2>
  <div class="abs platform"><i></i>ReviewNest</div>
  <div class="abs rule"></div>
  <blockquote class="abs">Quick, professional service. Had our water heater replaced same day!</blockquote>
  <div class="abs arrow" style="left:249px;background:#eee"><svg width="28" height="28" viewBox="0 0 28 28"><path d="M16 9l-5 5 5 5" fill="none" stroke="#fff" stroke-width="2"/></svg></div>
  <div class="abs arrow" style="left:925px;background:var(--royal)"><svg width="28" height="28" viewBox="0 0 28 28"><path d="M9 14h10M15 10l4 4-4 4" fill="none" stroke="#fff" stroke-width="2"/></svg></div>
  <div class="abs name">Mark T</div>
  <div class="abs place">West Palm Beach</div>
  <div class="abs stars">
    <svg width="110" height="20" viewBox="0 0 110 20" fill="#f5b82e"><path id="s" d="M10 1l2.7 5.6 6.1.8-4.4 4.2 1.1 6.1L10 14.8 4.5 17.7l1.1-6.1L1.2 7.4l6.1-.8z"/><use href="#s" x="22"/><use href="#s" x="44"/><use href="#s" x="66"/><use href="#s" x="88"/></svg>
  </div>
  <div class="abs dots"><i class="on"></i><i></i><i></i><i></i></div>
</section>

<section class="contact">
  <h2 class="abs">Get in Touch Now</h2>
  <p class="abs sub">Serving All of Palm Beach County, FL Contact us now to book your Same Day Service</p>
  <div class="abs map" role="img" aria-label="Satellite map of Palm Beach County service area">
    <div class="abs label"><svg width="14" height="18" viewBox="0 0 14 18"><path d="M7 18S0 10 0 7a7 7 0 0 1 14 0c0 3-7 11-7 11z" fill="#fff"/><circle cx="7" cy="7" r="2.5" fill="#2f3b33"/></svg>Area Map</div>
    <div class="abs pin"><svg width="12" height="16" viewBox="0 0 14 18"><path d="M7 18S0 10 0 7a7 7 0 0 1 14 0c0 3-7 11-7 11z" fill="#fff"/></svg></div>
    <div class="abs note">We already 24 hours fast services to help you. You can CALL US at &nbsp;<u>(555) 014-2278</u></div>
  </div>
  <form class="abs quote">
    <h3 class="abs">Request Your Free Quote</h3>
    <div class="abs" style="left:36px;top:112px;width:266px"><label>Name*</label><div class="field">Full Name</div></div>
    <div class="abs" style="left:316px;top:112px;width:266px"><label>Phone*</label><div class="field">Phone Number</div></div>
    <div class="abs" style="left:36px;top:191px;width:546px"><label>Email*</label><div class="field">Email Address</div></div>
    <div class="abs" style="left:36px;top:280px;width:546px"><label>Service Type</label><div class="field select">Gas Water Heater<svg width="10" height="6" viewBox="0 0 10 6"><path d="M1 1l4 4 4-4" fill="none" stroke="#555" stroke-width="1.3"/></svg></div></div>
    <div class="abs" style="left:36px;top:368px;width:546px"><label>Tell us About your Needs</label><div class="field area">Your Message...</div></div>
    <a class="abs btn btn-solid submit">Get your Free Quote <svg width="14" height="10" viewBox="0 0 14 10"><path d="M0 5h12M8 1l4 4-4 4" fill="none" stroke="#fff" stroke-width="1.5"/></svg></a>
  </form>
</section>

<section class="cta">
  <h2 class="abs">Ready to Book Expert Water Heater Service with Warranties That Last.</h2>
  <div class="abs links">Installation <i></i> Repair <i></i> Replacements</div>
  <a class="abs btn btn-solid">Call Us Now <span class="ring"><svg width="14" height="14" viewBox="0 0 24 24" fill="#ee7325"><path d="M6.6 10.8a15 15 0 0 0 6.6 6.6l2.2-2.2c.3-.3.7-.4 1-.2 1.1.4 2.3.6 3.6.6.6 0 1 .4 1 1V20c0 .6-.4 1-1 1A17 17 0 0 1 3 4c0-.6.4-1 1-1h3.5c.6 0 1 .4 1 1 0 1.3.2 2.5.6 3.6.1.3 0 .7-.2 1z"/></svg></span></a>
  <div class="abs photo" role="img" aria-label="Technician giving a thumbs up between tankless and tank water heaters"></div>
</section>

<footer class="site-footer">
  <div class="contact-row">
    <div class="abs c" style="left:120px"><div class="ico"><svg width="18" height="18" viewBox="0 0 24 24" fill="#ee7325"><path d="M6.6 10.8a15 15 0 0 0 6.6 6.6l2.2-2.2c.3-.3.7-.4 1-.2 1.1.4 2.3.6 3.6.6.6 0 1 .4 1 1V20c0 .6-.4 1-1 1A17 17 0 0 1 3 4c0-.6.4-1 1-1h3.5c.6 0 1 .4 1 1 0 1.3.2 2.5.6 3.6.1.3 0 .7-.2 1z"/></svg></div><div><small>Phone Number</small><span>(555)-0142-7781</span></div></div>
    <div class="abs c" style="left:468px"><div class="ico"><svg width="16" height="20" viewBox="0 0 14 18"><path d="M7 18S0 10 0 7a7 7 0 0 1 14 0c0 3-7 11-7 11z" fill="#ee7325"/><circle cx="7" cy="7" r="2.5" fill="#1d2340"/></svg></div><div><small>Office Address</small><span>Palm Beach County Florida</span></div></div>
    <div class="abs c" style="left:864px"><div class="ico"><svg width="18" height="14" viewBox="0 0 24 18"><path d="M0 0h24v18H0z" fill="#ee7325"/><path d="M0 0l12 9 12-9" stroke="#1d2340" stroke-width="2" fill="none"/></svg></div><div><small>Email Address</small><span>info@sirflowboiler.com</span></div></div>
  </div>
  <div class="abs brand"><span class="dot"></span>Sir FlowBoiler</div>
  <div class="abs col" style="left:302px"><h4>Quick Links</h4><ul><li>Home</li><li>Gas Water Heaters</li><li>Electric Water Heaters</li><li>Tankless Water Heaters</li></ul></div>
  <div class="abs col" style="left:498px"><h4>Company</h4><ul><li>About Us</li><li>Contact</li><li>Privacy Policy</li><li>Terms and Conditions</li></ul></div>
  <div class="abs col" style="left:676px"><h4>Follow Us On :</h4><div class="social"><i></i><i></i><i></i><i></i><i></i></div></div>
  <div class="abs copy">© 2026 Sir FlowBoiler. All rights reserved. | Licensed &amp; Insured</div>
</footer>

</body>
</html>
```